Vardel Precision New Website Design

We just changed our logo (thank you ArtFolkly) and company name change from Vardel Precision Machining to Vardel Precision Manufacturing. We do CNC Swiss screw machining and multi-axis machines. We make parts for many industries. We make large quantity production parts as well small R&D quantities. You can look at our current (outdated) website: http://www.vardelprecisionmachining.example to see what we do. We would like a WordPress site, including contact form for "request for quote" . We would also like it to be mobile friendly, and the ability to maintain it ourselves after it is finished I have included our new logo and fonts for references. We would like our site to convey the feeling of precision, capability, and trust worthiness with a very modern look. The new website address is www.vardelprec-mfg.example

Font styles to use
Serif
Sans Serif
Other font styles liked:
• fronts included, not sure if they work

Colors

Designer to choose colors to be used in the design.

Requirements
Must have
• Contact Info, request for quote field

```html
<!DOCTYPE html>
<html lang="en">
<head>
<meta charset="utf-8">
<title>Vardel Precision Manufacturing</title>
<link href="https://fonts.googleapis.com/css2?family=Playfair+Display:wght@400;700&family=Roboto:wght@300;400;500&display=swap" rel="stylesheet">
<style>
:root{
  --teal:#0c5f6e;
  --teal-dark:#084854;
  --teal-bright:#1c8ea0;
  --ink:#1b1b1b;
  --muted:#555;
  --white:#fff;
  --paper:#f3f3f3;
  --footer-bar:#06323b;
  --star:#f2b400;
}
*{box-sizing:border-box;margin:0;padding:0}
html,body{width:1200px;height:3136px;overflow:hidden}
body{font-family:"Roboto",Arial,sans-serif;color:var(--ink);background:var(--white);position:relative}
.abs{position:absolute}
.serif{font-family:"Playfair Display",Georgia,serif}
section,header,footer{position:absolute;left:0;width:1200px}

/* hero */
.hero{top:0;height:565px;background:radial-gradient(ellipse at 70% 55%,#5b5f63 0%,#2a2d30 40%,#0d0e10 80%)}
.brand{left:226px;top:22px;display:flex;align-items:center;gap:10px;color:var(--white)}
.brand-mark{width:34px;height:34px;border:2px solid var(--white);border-radius:50%}
.brand-name{font-family:"Playfair Display",Georgia,serif;font-size:20px;font-weight:700;line-height:1}
.call{left:770px;top:25px;height:30px;width:146px;border-radius:15px;background:var(--white);display:flex;align-items:center;font-size:11px}
.call b{background:var(--teal);color:var(--white);font-family:"Playfair Display",Georgia,serif;font-weight:400;height:30px;line-height:30px;padding:0 10px;border-radius:15px 0 0 15px}
.call span{padding-left:8px;display:flex;align-items:center;gap:5px}
.socials{display:flex;gap:9px}
.social{width:20px;height:20px;border-radius:50%;border:1.5px solid currentColor}
.hero .socials{left:873px;top:66px;color:var(--white)}
.nav{left:540px;top:95px;display:flex;gap:38px;color:var(--white);font-size:12px;font-weight:500}
.quote{left:397px;top:174px;width:408px;height:303px;background:rgba(12,95,110,.88);border-radius:10px;color:var(--white);text-align:center;padding-top:22px}
.quote h1{font-family:"Playfair Display",Georgia,serif;font-weight:400;font-size:25px}
.quote p{font-size:11px;line-height:1.3;width:300px;margin:10px auto 0}
.quote h2{font-family:"Playfair Display",Georgia,serif;font-weight:400;font-size:19px;margin-top:14px}
.field{position:absolute;border-bottom:1px solid rgba(255,255,255,.7);font-size:9px;text-align:left;padding-bottom:4px;color:rgba(255,255,255,.85)}
.send{position:absolute;left:130px;top:234px;width:146px;height:37px;background:#0b2024;font-family:"Playfair Display",Georgia,serif;font-size:13px;line-height:37px}
.dots{display:flex;gap:5px;justify-content:center}
.dot{width:8px;height:8px;border-radius:50%;background:#8a8a8a}
.dot.on{width:11px;height:11px;border:2px solid var(--white);background:transparent;margin-top:-1px}
.hero .dots{left:0;width:1200px;top:506px}

/* about */
.about{top:565px;height:418px;background:linear-gradient(90deg,#e9e9e9,#f7f7f7 50%,#ececec)}
.about-ring1{left:260px;top:80px;width:150px;height:150px;border-radius:50%;background:var(--teal)}
.about-ring2{left:490px;top:230px;width:95px;height:95px;border-radius:50%;background:var(--teal-bright)}
.about-photo{left:280px;top:62px;width:240px;height:240px;border-radius:50%;background:radial-gradient(circle at 45% 45%,#d8d2c4,#8b7f6a 55%,#3d3a36);border:6px solid var(--white)}
h2.title{font-family:"Playfair Display",Georgia,serif;font-weight:700;font-size:29px;color:var(--ink)}
h2.title em{font-style:normal;color:var(--teal)}
.rule{display:block;width:60px;height:8px;margin-top:4px}
.about-text{left:623px;top:76px;width:360px}
.about-text p{font-size:10.5px;line-height:1.35;color:var(--muted);margin-top:12px}
.read{font-family:"Playfair Display",Georgia,serif;font-size:11px;color:var(--teal);font-weight:700;margin-top:14px;display:block}

.center{left:0;width:1200px;text-align:center}
.center .rule{margin:4px auto 0}
.lead{font-size:11px;line-height:1.35;color:var(--muted);width:640px;margin:10px auto 0}

/* industries */
.industries{top:983px;height:617px;background:var(--white)}
.ind{position:absolute;width:160px;margin-left:-80px;text-align:center}
.ind svg{display:block;margin:0 auto}
.ind span{font-family:"Playfair Display",Georgia,serif;font-size:18px;display:block;margin-top:2px}
.ind.hl span{color:var(--teal)}
.btn{position:absolute;left:531px;top:445px;width:138px;height:46px;border-radius:10px;background:var(--teal);color:var(--white);font-family:"Playfair Display",Georgia,serif;font-size:13px;line-height:46px;text-align:center}

/* work */
.work{top:1600px;height:445px;background:var(--teal);color:var(--white)}
.work-badge{left:556px;top:-76px;width:88px;height:88px;border-radius:50%;background:var(--teal);border:4px solid var(--white);box-shadow:0 0 0 6px var(--teal)}
.work h2.title{color:var(--white)}
.work .lead{color:#dfeef0}
.tile{position:absolute;overflow:hidden}
.cap{position:absolute;left:0;bottom:10px;background:rgba(0,0,0,.75);color:var(--white);font-size:8px;padding:4px 24px 4px 6px;font-family:"Playfair Display",Georgia,serif}
.cap::after{content:"›";position:absolute;right:6px;top:0;font-size:13px}
.scroll{left:298px;top:394px;width:604px;height:3px;background:rgba(255,255,255,.35)}
.scroll i{position:absolute;left:0;top:-1px;width:130px;height:5px;background:#9bb9bf}

/* services */
.services{top:2045px;height:485px;background:linear-gradient(180deg,#f1f1f1,#fafafa 60%,#eeeeee)}
.svc{position:absolute;width:170px;margin-left:-85px;text-align:center}
.svc .ico{width:86px;height:86px;border-radius:50%;background:var(--white);margin:0 auto;display:flex;align-items:center;justify-content:center;box-shadow:0 2px 8px rgba(0,0,0,.12)}
.svc.hl .ico{border:2px solid var(--teal)}
.svc span{display:block;font-family:"Playfair Display",Georgia,serif;font-size:16px;line-height:1.15;margin-top:12px}
.svc.hl span{color:var(--teal)}
.svc-copy{left:270px;width:660px;top:358px;text-align:center;font-size:10.5px;line-height:1.35;color:var(--muted)}

/* testimonial */
.testimonial{top:2530px;height:338px;background:var(--white)}
.qmark{font-family:"Playfair Display",Georgia,serif;font-size:60px;color:#e2e2e2;line-height:1}
.say{font-size:16px;color:#333;width:640px;margin:0 auto;line-height:1.35}
.stars{color:var(--star);font-size:11px;letter-spacing:2px;margin-top:8px}
.who{font-family:"Playfair Display",Georgia,serif;color:var(--teal);font-size:13px;font-weight:700}
.role{font-family:"Playfair Display",Georgia,serif;color:var(--teal);font-size:12px}
.testimonial .dot.on{border-color:var(--teal)}
.testimonial .dot{background:#c8c8c8}

/* footer */
.footer{top:2868px;height:222px;background:var(--teal);color:var(--white)}
.footer .brand{left:282px;top:27px}
.foot-about{left:282px;top:86px;width:196px;font-size:10px;line-height:1.3}
.col{position:absolute;top:42px}
.col h3{font-family:"Playfair Display",Georgia,serif;font-weight:700;font-size:12px}
.col h3::after{content:"";display:block;width:70px;height:2px;background:var(--white);margin-top:6px}
.col ul{list-style:none;margin-top:8px}
.col li{font-size:10px;height:23.5px;display:flex;align-items:center;gap:7px}
.col li::before{content:"";width:5px;height:5px;border-radius:50%;background:var(--white)}
.contact li{height:auto;align-items:flex-start;margin-bottom:10px;line-height:1.3}
.contact li::before{display:none}
.contact svg{flex:none;margin-top:1px}
.footer .socials{margin-top:10px}
.badges{display:flex;gap:10px;margin-top:8px}
.badge{width:34px;height:34px;background:#d9d9d9}
.badge.round{border-radius:50%}
.bottom{top:3090px;height:46px;background:var(--footer-bar);color:var(--white);font-size:11px;text-align:center;line-height:46px}
</style>
</head>
<body>

<header class="hero" role="img" aria-label="Close-up photograph of a precision machined metal part and spindle" >
  <div class="abs brand"><span class="brand-mark"></span><span class="brand-name">Vardel Precision</span></div>
  <div class="abs call"><b>Call us Today</b><span>
    <svg width="10" height="10" viewBox="0 0 24 24"><path d="M6.6 10.8a15 15 0 0 0 6.6 6.6l2.2-2.2c.3-.3.7-.4 1-.2 1.1.4 2.3.6 3.6.6.6 0 1 .4 1 1V20c0 .6-.4 1-1 1A17 17 0 0 1 3 4c0-.6.4-1 1-1h3.5c.6 0 1 .4 1 1 0 1.3.2 2.5.6 3.6.1.3 0 .7-.2 1z" fill="#333"/></svg>858-410-2278</span></div>
  <div class="abs socials"><i class="social"></i><i class="social"></i><i class="social"></i><i class="social"></i></div>
  <nav class="abs nav"><span>Services</span><span>Equipment</span><span>Quality</span><span>Our work</span><span>About us</span><span>Contact us</span></nav>
  <form class="abs quote">
    <h1>Your Part , Your Design , Your Way</h1>
    <p>Vardel Precision Machining Company is a high quality machining resource providing friendly service, fast turnaround times, and engineering expertise, at competitive pricing</p>
    <h2>Request a quote</h2>
    <div class="field" style="left:22px;top:160px;width:170px">Your name</div>
    <div class="field" style="left:216px;top:160px;width:170px">Email</div>
    <div class="field" style="left:22px;top:192px;width:364px;height:26px">Message</div>
    <div class="send">Send</div>
  </form>
  <div class="abs dots"><i class="dot on"></i><i class="dot"></i><i class="dot"></i><i class="dot"></i></div>
</header>

<section class="about">
  <div class="abs about-ring1"></div>
  <div class="abs about-ring2"></div>
  <div class="abs about-photo" role="img" aria-label="Photograph of a milling cutter with carbide inserts and a drill bit"></div>
  <div class="abs about-text">
    <h2 class="title">About <em>us</em></h2>
    <svg class="rule" viewBox="0 0 60 8"><path d="M0 6 Q30 -2 60 6" stroke="#0c5f6e" stroke-width="2.5" fill="none"/></svg>
    <p>Founded in 1996, Vardel Precision Machining Inc. was established at the hands of engineering experts, trying to develop a high quality solution for the machining industry. Vardel Precision Machining Inc. utilizes state of the art, fully automated, equipment. This enables us to provide quick turnaround times, without compromising the quality of the product.</p>
    <p>We prides ourselves on our friendly and efficient customer service; making sure we meet the needs and standards of our valuable customers. With a knowledgeable team, we provide companies with invaluable support during the engineering process; producing favorable results and always leave customers extremely gratified.</p>
    <p>Here at Vardel Precision, we strive to provide our clients with loyalty in a partner, where a handshake is more than a greeting; it is the hopeful development of a strong relationship.</p>
    <span class="read">Read More &#8594;</span>
  </div>
</section>

<section class="industries">
  <div class="abs center" style="top:52px">
    <h2 class="title">Industries <em>served</em></h2>
    <svg class="rule" viewBox="0 0 60 8"><path d="M0 6 Q30 -2 60 6" stroke="#0c5f6e" stroke-width="2.5" fill="none"/></svg>
    <p class="lead">Vardel Precision Machining Company is a high quality machining resource providing friendly service, fast turnaround times, and engineering expertise, at competitive pricing</p>
  </div>

  <div class="ind" style="left:360px;top:172px">
    <svg width="90" height="64" viewBox="0 0 90 64"><path d="M5 60 A40 40 0 0 1 85 60" stroke="#0c5f6e" stroke-width="3" fill="none"/><path d="M45 22 l3 12 14 6 v3 l-14-3 -1 9 4 3 v2 l-6-2 -6 2 v-2 l4-3 -1-9 -14 3 v-3 l14-6z" fill="#0c5f6e"/></svg>
    <span>Aerospace</span></div>
  <div class="ind hl" style="left:600px;top:172px">
    <svg width="90" height="64" viewBox="0 0 90 64"><path d="M5 60 A40 40 0 0 1 85 60" stroke="#0c5f6e" stroke-width="3" fill="none"/><rect x="34" y="24" width="22" height="30" rx="2" fill="#0c5f6e"/><rect x="38" y="30" width="14" height="10" fill="#fff"/><circle cx="45" cy="47" r="3" fill="#fff"/></svg>
    <span>Electronics</span></div>
  <div class="ind" style="left:838px;top:172px">
    <svg width="90" height="64" viewBox="0 0 90 64"><path d="M5 60 A40 40 0 0 1 85 60" stroke="#0c5f6e" stroke-width="3" fill="none"/><path d="M30 36 h30 v12 h-30z M38 28 h16 l4 8 h-24z" fill="#0c5f6e"/><circle cx="36" cy="50" r="4" fill="#0c5f6e"/><circle cx="54" cy="50" r="4" fill="#0c5f6e"/></svg>
    <span>Automotive</span></div>
  <div class="ind" style="left:360px;top:300px">
    <svg width="90" height="64" viewBox="0 0 90 64"><path d="M5 60 A40 40 0 0 1 85 60" stroke="#0c5f6e" stroke-width="3" fill="none"/><circle cx="45" cy="22" r="4" stroke="#0c5f6e" stroke-width="2.5" fill="none"/><path d="M45 26 v28 M37 32 h16 M33 44 q12 14 24 0" stroke="#0c5f6e" stroke-width="3" fill="none"/></svg>
    <span>Marine</span></div>
  <div class="ind hl" style="left:600px;top:300px">
    <svg width="90" height="64" viewBox="0 0 90 64"><path d="M5 60 A40 40 0 0 1 85 60" stroke="#0c5f6e" stroke-width="3" fill="none"/><rect x="30" y="22" width="24" height="18" fill="#0c5f6e"/><rect x="33" y="25" width="18" height="12" fill="#fff"/><rect x="38" y="42" width="8" height="4" fill="#0c5f6e"/><rect x="32" y="46" width="20" height="3" fill="#0c5f6e"/><rect x="57" y="24" width="7" height="25" fill="#0c5f6e"/></svg>
    <span>Computer</span></div>
  <div class="ind" style="left:838px;top:300px">
    <svg width="90" height="64" viewBox="0 0 90 64"><path d="M5 60 A40 40 0 0 1 85 60" stroke="#0c5f6e" stroke-width="3" fill="none"/><path d="M34 26 q11-6 22 0 q4 10 -2 16 l-3 12 -4-10 h-4 l-4 10 -3-12 q-6-6 -2-16z" fill="#0c5f6e"/></svg>
    <span>Dental</span></div>

  <div class="btn">View More</div>
</section>

<section class="work">
  <div class="abs work-badge" style="display:flex;align-items:center;justify-content:center">
    <svg width="36" height="30" viewBox="0 0 36 30"><rect x="2" y="2" width="32" height="26" rx="3" fill="#fff"/><path d="M6 24 l9-10 6 6 4-4 6 8z" fill="#0c5f6e"/><circle cx="25" cy="9" r="3" fill="#0c5f6e"/></svg>
  </div>
  <div class="abs center" style="top:24px">
    <h2 class="title">Our Work</h2>
    <svg class="rule" viewBox="0 0 60 8"><path d="M0 6 Q30 -2 60 6" stroke="#fff" stroke-width="2.5" fill="none"/></svg>
    <p class="lead">Vardel Precision has provided some of the most innovative results for clients, among many different industries. Below are just some of the quality products we were able to produce:</p>
  </div>
  <div class="tile" style="left:226px;top:139px;width:144px;height:226px;background:linear-gradient(160deg,#cfe3f0,#4e8fb8 60%,#22506e)" role="img" aria-label="Photograph of steel bolts and nuts in water"><span class="cap">Lorem Ipsum is simply</span></div>
  <div class="tile" style="left:374px;top:139px;width:144px;height:110px;background:linear-gradient(150deg,#8e9296,#3a3d40 60%,#111)" role="img" aria-label="Photograph of hex bolts"><span class="cap">Lorem Ipsum is simply</span></div>
  <div class="tile" style="left:374px;top:253px;width:144px;height:112px;background:linear-gradient(150deg,#b07a4c,#6b4526 60%,#3a2414)" role="img" aria-label="Photograph of machined fasteners on wood"><span class="cap">Lorem Ipsum is simply</span></div>
  <div class="tile" style="left:524px;top:139px;width:254px;height:226px;background:radial-gradient(circle at 50% 45%,#9a9a98,#5c5c5a 60%,#333)" role="img" aria-label="Photograph of hex nuts, washers and bolts on a grey surface"><span class="cap">Lorem Ipsum is simply dummy text of the</span></div>
  <div class="tile" style="left:782px;top:139px;width:192px;height:110px;background:linear-gradient(150deg,#5a84c4,#24498a 60%,#0f2550)" role="img" aria-label="Photograph of screws on a blue background"><span class="cap">Lorem Ipsum is simply</span></div>
  <div class="tile" style="left:782px;top:253px;width:192px;height:112px;background:linear-gradient(150deg,#f2f2f2,#a8a8a8 60%,#4d4d4d)" role="img" aria-label="Photograph of machined pins on white"><span class="cap">Lorem Ipsum is simply</span></div>
  <div class="abs scroll"><i></i></div>
</section>

<section class="services">
  <div class="abs center" style="top:52px">
    <h2 class="title">Our <em>Services</em></h2>
    <svg class="rule" viewBox="0 0 60 8"><path d="M0 6 Q30 -2 60 6" stroke="#0c5f6e" stroke-width="2.5" fill="none"/></svg>
    <p class="lead">Providing you with honest straightforward service is our number one goal. We manufacture finished metal and plastic goods to tight tolerances using technologically advanced equipment</p>
  </div>
  <div class="svc" style="left:433px;top:184px"><div class="ico">
    <svg width="40" height="40" viewBox="0 0 40 40" fill="none" stroke="#222" stroke-width="1.8"><path d="M20 12 l8 4 v8 l-8 4 -8-4 v-8z M12 16 l8 4 8-4 M20 20 v8"/><path d="M20 3 v6 M20 31 v6 M4 12 l5 3 M36 12 l-5 3 M4 28 l5-3 M36 28 l-5-3"/></svg></div>
    <span>Part<br>Production</span></div>
  <div class="svc hl" style="left:604px;top:184px"><div class="ico">
    <svg width="40" height="40" viewBox="0 0 40 40" fill="none" stroke="#222" stroke-width="2"><path d="M8 22 v-4 a12 12 0 0 1 24 0 v4"/><rect x="6" y="21" width="6" height="10" rx="2"/><rect x="28" y="21" width="6" height="10" rx="2"/><path d="M31 31 q0 5 -8 5 h-3"/></svg></div>
    <span>Engineering<br>Assistance</span></div>
  <div class="svc" style="left:778px;top:184px"><div class="ico">
    <svg width="40" height="40" viewBox="0 0 40 40" fill="none" stroke="#222" stroke-width="1.8"><path d="M20 16 l9 4.5 v9 l-9 4.5 -9-4.5 v-9z M11 20.5 l9 4.5 9-4.5 M20 25 v9"/><path d="M20 4 v8 M14 8 l6-4 6 4"/></svg></div>
    <span>Outside Process<br>Coordination</span></div>
  <div class="abs svc-copy">
    <p>For producing other machined possibilities 3, 4 and 5-axis milling, horizontal or vertical with up to 64" x 32" x 35" (XYZ) capacity are also ready to fulfill your needs. With turning capabilities to 15" X 32" (Diameter &amp; Length) our Mill Turn Centers offer up to 3 turrets / 8 axis, live tool mill/turn capability for increased efficiency on complex parts.</p>
    <p style="margin-top:14px">Materials include but not limited to, all austenitic and martensitic stainless steels, Titanium, Aluminum, Brass, nickel and heat resistant alloys and the full spectrum of engineered plastics and composites.</p>
  </div>
</section>

<section class="testimonial">
  <div class="abs center" style="top:52px">
    <h2 class="title">Client <em>Testimonial</em></h2>
    <svg class="rule" viewBox="0 0 60 8"><path d="M0 6 Q30 -2 60 6" stroke="#0c5f6e" stroke-width="2.5" fill="none"/></svg>
    <div class="qmark">&#8220;</div>
    <p class="say">"I love working with engineers. Finding ways to make their parts less expensive is a puzzle I never get tired of solving."</p>
    <div class="stars">&#9733;&#9733;&#9733;&#9733;&#9733;</div>
    <div class="who">Tomas Bellweather</div>
    <div class="role">Founder</div>
    <div class="dots" style="margin-top:8px"><i class="dot on"></i><i class="dot"></i><i class="dot"></i><i class="dot"></i></div>
  </div>
</section>

<footer class="footer">
  <div class="abs brand"><span class="brand-mark"></span><span class="brand-name">Vardel Precision</span></div>
  <p class="abs foot-about">Founded in 1996, Vardel Precision Machining Inc. was established at the hands of engineering experts, trying to develop a high quality solution for the machining industry. Vardel Precision Machining Inc. utilizes state of the art, fully automated, equipment. This enables us to provide quick turnaround times, without compromising the quality of the product.</p>
  <div class="col" style="left:537px">
    <h3>Site map</h3>
    <ul><li>Services</li><li>Equipment</li><li>Quality</li><li>Our work</li><li>About us</li><li>Contact us</li></ul>
  </div>
  <div class="col contact" style="left:642px">
    <h3>Contact us</h3>
    <ul style="margin-top:14px">
      <li><svg width="10" height="13" viewBox="0 0 10 13"><path d="M5 0a5 5 0 0 1 5 5c0 3.5-5 8-5 8S0 8.5 0 5a5 5 0 0 1 5-5z" fill="#fff"/><circle cx="5" cy="5" r="1.8" fill="#0c5f6e"/></svg><span>Vardel Precision Machining<br>4410 Kettner Way<br>Harbor City, CA 90000</span></li>
      <li><svg width="11" height="11" viewBox="0 0 24 24"><path d="M6.6 10.8a15 15 0 0 0 6.6 6.6l2.2-2.2c.3-.3.7-.4 1-.2 1.1.4 2.3.6 3.6.6.6 0 1 .4 1 1V20c0 .6-.4 1-1 1A17 17 0 0 1 3 4c0-.6.4-1 1-1h3.5c.6 0 1 .4 1 1 0 1.3.2 2.5.6 3.6.1.3 0 .7-.2 1z" fill="#fff"/></svg><span>858-410-2290</span></li>
      <li><svg width="11" height="11" viewBox="0 0 12 12"><rect x="1" y="3" width="10" height="7" fill="none" stroke="#fff"/><rect x="3" y="1" width="6" height="3" fill="#fff"/></svg><span>858-410-2291</span></li>
      <li><svg width="12" height="10" viewBox="0 0 12 10"><rect x=".5" y=".5" width="11" height="9" fill="none" stroke="#fff"/><path d="M.5 .5 L6 5.5 11.5 .5" fill="none" stroke="#fff"/></svg><span>info@vardelprecision.example</span></li>
    </ul>
  </div>
  <div class="col" style="left:815px">
    <h3>Follow us</h3>
    <div class="socials"><i class="social"></i><i class="social"></i><i class="social"></i><i class="social"></i></div>
    <div class="badges"><i class="badge"></i><i class="badge round"></i><i class="badge round"></i></div>
  </div>
</footer>
<div class="abs bottom" style="left:0;width:1200px">&#169; All rights reserved</div>

</body>
</html>
```